Weinetiketten für unsere neue Weinlinie VELMORINA
Zielgruppe
Wir stellen qualitativ sehr hochwertige Weine, Sekte und Destillate her.
Unsere Zielgruppe sind kaufkräftige Kunden zwischen 25-70 Jahren.
Aufgabenstellung
Edel, schlicht und zeitlos soll das neue Etikett werden, nur leicht verspielt.
Mit hohem Wiedererkennungswert, da die Wein auch im Fachhandel (in Regalen) präsentiert werden. Der Name "Velmorina" steht für expressive Weine voller Fruchtaromen und Düften.

```html
<!DOCTYPE html>
<html lang="de">
<head>
<meta charset="utf-8">
<title>Velmorina Lumen – Riesling trocken 2009</title>
<link rel="stylesheet" href="https://fonts.googleapis.com/css2?family=Kaushan+Script&family=Lato:wght@300;400&family=Playfair+Display:wght@400&display=swap">
<style>
  :root {
    --backdrop: #a4a4a4;
    --label-light: #f4f4f4;
    --label-shade: #dcdcdc;
    --ink: #1c1a1a;
    --gold: #c2ab72;
    --vintage: #8a5a12;
  }
  html, body {
    margin: 0;
    padding: 0;
    width: 1200px;
    height: 3001px;
    overflow: hidden;
    background: var(--backdrop);
  }
  .canvas {
    position: relative;
    width: 1200px;
    height: 3001px;
  }
  .wine-label {
    position: absolute;
    left: 65px;
    top: 500px;
    width: 1070px;
    height: 1980px;
    background: linear-gradient(180deg, var(--label-light) 0%, var(--label-light) 55%, var(--label-shade) 100%);
    text-align: center;
    color: var(--ink);
  }
  .maker-mark {
    position: absolute;
    left: 0;
    right: 0;
    top: 220px;
    display: flex;
    flex-direction: column;
    align-items: center;
    gap: 34px;
  }
  .maker-mark__dot {
    width: 150px;
    height: 150px;
    border-radius: 50%;
    background: var(--gold);
  }
  .maker-mark__name {
    font-family: "Lato", sans-serif;
    font-weight: 400;
    font-size: 58px;
    letter-spacing: 6px;
    color: var(--ink);
  }
  .wine-name {
    position: absolute;
    left: 0;
    right: 0;
    top: 720px;
    margin: 0;
    font-family: "Kaushan Script", cursive;
    font-weight: 400;
    font-size: 210px;
    line-height: 1;
    color: var(--ink);
  }
  .wine-line {
    position: absolute;
    left: 0;
    right: 0;
    top: 1010px;
    margin: 0;
    font-family: "Lato", sans-serif;
    font-weight: 300;
    font-size: 80px;
    letter-spacing: 18px;
    line-height: 1;
    color: var(--gold);
    text-indent: 18px;
  }
  .grape {
    position: absolute;
    left: 0;
    right: 0;
    top: 1520px;
    margin: 0;
    font-family: "Kaushan Script", cursive;
    font-size: 120px;
    line-height: 1.1;
    color: var(--ink);
  }
  .style {
    position: absolute;
    left: 0;
    right: 0;
    top: 1690px;
    margin: 0;
    font-family: "Lato", sans-serif;
    font-weight: 400;
    font-size: 50px;
    line-height: 1;
    color: var(--ink);
  }
  .vintage {
    position: absolute;
    left: 0;
    right: 0;
    top: 1780px;
    margin: 0;
    font-family: "Playfair Display", serif;
    font-size: 72px;
    line-height: 1;
    color: var(--vintage);
  }
</style>
</head>
<body>
<main class="canvas">
  <section class="wine-label">
    <div class="maker-mark">
      <span class="maker-mark__dot"></span>
      <span class="maker-mark__name">Haus Kelmer</span>
    </div>
    <h1 class="wine-name">Velmorina</h1>
    <p class="wine-line">LUMEN</p>
    <p class="grape">riesling</p>
    <p class="style">trocken</p>
    <p class="vintage">2009</p>
  </section>
</main>
</body>
</html>
```